Refresh of Business Card Design

Want to refresh the business card design with the new logo while adhering to style guide as attached. Would like to match feel of website www.durmackvinex.com

```html
<!DOCTYPE html>
<html lang="en">
<head>
<meta charset="utf-8">
<title>Durmack Vinex – Business Card</title>
<link rel="stylesheet" href="https://fonts.googleapis.com/css2?family=Work+Sans:wght@400;500;700&display=swap">
<style>
  :root {
    --stage: #6b6b6b;
    --card: #000000;
    --brand-red: #e8214a;
    --ink-light: #ffffff;
    --ink-soft: #e6e6e6;
    --font: "Work Sans", Arial, sans-serif;
  }
  * { box-sizing: border-box; margin: 0; padding: 0; }
  html, body {
    width: 1200px; height: 1200px; overflow: hidden;
    background: var(--stage);
    font-family: var(--font);
  }
  .canvas { position: relative; width: 1200px; height: 1200px; }

  .card {
    position: absolute;
    width: 699px; height: 419px;
    background: var(--card);
    overflow: hidden;
  }
  .card--front { left: 249px; top: 116px; }
  .card--back  { left: 250px; top: 645px; }

  .band {
    position: absolute; left: 0; right: 0;
    background: var(--brand-red);
  }
  .card--front .band { top: 164px; height: 81px; }
  .card--back  .band { top: 90px;  height: 82px; }

  .wordmark {
    position: absolute;
    color: var(--ink-light);
    font-weight: 700;
    font-size: 30px;
    letter-spacing: 1px;
    white-space: nowrap;
    transform: translate(-50%, -50%);
    display: flex; align-items: center; gap: 12px;
  }
  .wordmark__dot {
    width: 18px; height: 18px; border-radius: 50%;
    background: var(--ink-light);
  }
  .card--front .wordmark { left: 350px; top: 204px; }
  .card--back  .wordmark { left: 188px; top: 131px; font-size: 27px; }

  .front-url {
    position: absolute; left: 0; right: 0; top: 354px;
    text-align: center;
    color: var(--ink-light);
    font-size: 20px;
    letter-spacing: 13px;
    padding-left: 13px;
  }

  .person {
    position: absolute; right: 48px; top: 100px;
    text-align: right; color: var(--ink-light);
  }
  .person__name { font-size: 31px; font-weight: 700; line-height: 1.1; letter-spacing: 0.5px; }
  .person__role { font-size: 18px; font-weight: 400; margin-top: 2px; }

  .contact-list, .address {
    position: absolute; list-style: none;
    color: var(--ink-soft); font-size: 18px;
  }
  .contact-list { left: 46px; top: 283px; }
  .contact-list li {
    display: flex; align-items: center; gap: 10px;
    height: 31px;
  }
  .icon { width: 18px; height: 18px; flex: none; fill: var(--brand-red); }

  .address { left: 406px; top: 285px; display: flex; gap: 10px; }
  .address p { line-height: 27px; }
  .address .icon { margin-top: 3px; }
</style>
</head>
<body>
<main class="canvas">

  <section class="card card--front" aria-label="Card front">
    <div class="band"></div>
    <div class="wordmark"><span class="wordmark__dot"></span>DURMACK VINEX</div>
    <p class="front-url">DURMACKVINEX.COM</p>
  </section>

  <section class="card card--back" aria-label="Card back">
    <div class="band"></div>
    <div class="wordmark"><span class="wordmark__dot"></span>DURMACK VINEX</div>
    <div class="person">
      <p class="person__name">REID CALLOWAY</p>
      <p class="person__role">SALES</p>
    </div>

    <ul class="contact-list">
      <li>
        <svg class="icon" viewBox="0 0 24 24" aria-hidden="true"><path d="M6.6 10.8a15.1 15.1 0 0 0 6.6 6.6l2.2-2.2a1 1 0 0 1 1-.25 11.4 11.4 0 0 0 3.6.57 1 1 0 0 1 1 1V20a1 1 0 0 1-1 1A17 17 0 0 1 3 4a1 1 0 0 1 1-1h3.5a1 1 0 0 1 1 1c0 1.25.2 2.45.57 3.6a1 1 0 0 1-.25 1z"/></svg>
        <span>806-555-0148</span>
      </li>
      <li>
        <svg class="icon" viewBox="0 0 24 24" aria-hidden="true"><path d="M3 5h18a1 1 0 0 1 1 1v12a1 1 0 0 1-1 1H3a1 1 0 0 1-1-1V6a1 1 0 0 1 1-1zm9 7.2L20.5 7h-17z"/></svg>
        <span>rcalloway@durmackvinex.com</span>
      </li>
      <li>
        <svg class="icon" viewBox="0 0 24 24" aria-hidden="true"><path d="M12 2a10 10 0 1 0 0 20 10 10 0 0 0 0-20zm6.9 6h-2.9a15.7 15.7 0 0 0-1.4-3.6A8 8 0 0 1 18.9 8zM12 4c.8 1.2 1.5 2.5 1.9 4h-3.8c.4-1.5 1.1-2.8 1.9-4zM4.3 14a8.2 8.2 0 0 1 0-4h3.4a16.5 16.5 0 0 0 0 4zm.8 2h2.9c.3 1.3.8 2.5 1.4 3.6A8 8 0 0 1 5.1 16zM8 8H5.1a8 8 0 0 1 4.3-3.6C8.8 5.5 8.3 6.7 8 8zm4 12c-.8-1.2-1.5-2.5-1.9-4h3.8c-.4 1.5-1.1 2.8-1.9 4zm2.3-6H9.7a14.7 14.7 0 0 1 0-4h4.6a14.7 14.7 0 0 1 0 4zm.3 5.6c.6-1.1 1.1-2.3 1.4-3.6h2.9a8 8 0 0 1-4.3 3.6zm1.7-5.6a16.5 16.5 0 0 0 0-4h3.4a8.2 8.2 0 0 1 0 4z"/></svg>
        <span>durmackvinex.com</span>
      </li>
    </ul>

    <div class="address">
      <svg class="icon" viewBox="0 0 24 24" aria-hidden="true"><path d="M12 2a7 7 0 0 0-7 7c0 5.2 7 13 7 13s7-7.8 7-13a7 7 0 0 0-7-7zm0 9.5A2.5 2.5 0 1 1 12 6.5a2.5 2.5 0 0 1 0 5z"/></svg>
      <p>40215 Lindale, TX79760.<br>72 Harbor Ln Ashby,<br>TX79123.</p>
    </div>
  </section>

</main>
</body>
</html>
```